Business Card design
Cordavera Ruvek Martial Arts Training Center
I need single sided standard sized Business Card [3.5" x 2"]
Font in logo is CGF Locust Resistance. This font does not need to be used.
Modern
Cordavera Ruvek or Cordavera Ruvek Martial Arts Training Center
Martial Arts Discipline | Disciplined Strength
2671 Bramble Rd
Kalamazoo, MI
info@cordaverix.example
www.cordaverix.example
facebook.com/cordaverix
optional items for the business card:
Pelnor Grappling League
Todd Weslin Jiu Jitsu
Orvane Kickboxing Union
Mixed Martial Arts
Fitness
Can put the logo on one side and the information on the second side if you would like to submit that type of design.
Cordavera Ruvek illustrator file
Cordavera Ruvek eps file

```html
<!DOCTYPE html>
<html lang="en">
<head>
<meta charset="utf-8">
<title>Cordavera Ruvek Stationery</title>
<link href="https://fonts.googleapis.com/css2?family=Titillium+Web:wght@400;700&display=swap" rel="stylesheet">
<style>
:root{
  --red:#e5262b;
  --grey:#9a9a9c;
  --light-grey:#d4d4d6;
  --ink:#555559;
  --paper:#ffffff;
  --backdrop:#ece8e3;
}
*{margin:0;padding:0;box-sizing:border-box}
html,body{width:1200px;height:846px;overflow:hidden}
body{background:var(--backdrop);font-family:"Titillium Web",Arial,sans-serif;color:var(--ink);position:relative}
.piece{position:absolute;background:var(--paper);overflow:hidden;box-shadow:0 2px 6px rgba(0,0,0,.18)}
.piece svg.shape{position:absolute;left:0;top:0}
.brand{position:absolute;display:flex;align-items:center;gap:8px;font-weight:700;letter-spacing:.5px;white-space:nowrap}
.brand .mark{display:block;background:var(--red)}
.brand-dark{color:var(--ink)}
.brand-white{color:#fff}
.brand-white .mark{background:#fff}
.contact{position:absolute;font-size:9px;line-height:1.35;color:var(--ink);font-style:normal;white-space:nowrap}
.contact b{color:var(--red);font-weight:700}
.web{position:absolute;left:0;right:0;text-align:center;font-size:10px;font-weight:700}
.faint-mark{position:absolute;background:var(--red);opacity:.12}

/* letterhead */
.letterhead{left:252px;top:29px;width:552px;height:763px}
.letterhead .brand{left:36px;top:50px;font-size:28px}
.letterhead .brand .mark{width:26px;height:26px}
.letterhead .contact{left:310px;top:22px}
.letterhead .faint-mark{left:-30px;top:300px;width:110px;height:110px}
.letterhead .web{bottom:12px;color:#fff}

/* red card */
.card{border-radius:14px}
.card-red{left:835px;top:43px;width:341px;height:197px;background:var(--red)}
.card-red .brand{left:0;right:0;justify-content:center;top:62px;font-size:22px}
.card-red .brand .mark{width:20px;height:20px}
.card-red .web{bottom:34px;color:#fff}

/* front card */
.card-front{left:43px;top:168px;width:348px;height:206px}
.card-front .owner{position:absolute;left:16px;top:14px;color:#fff}
.card-front .owner h1{font-size:13px;font-weight:700;line-height:1.1}
.card-front .owner p{font-size:8px}
.card-front .brand{left:150px;top:44px;font-size:17px}
.card-front .brand .mark{width:16px;height:16px}
.card-front .contact{left:16px;top:118px;color:#fff;font-size:8px}
.card-front .contact b{color:#fff}

/* white card */
.card-white{left:43px;top:391px;width:348px;height:192px}
.card-white .brand{left:0;right:0;justify-content:center;top:68px;font-size:22px}
.card-white .brand .mark{width:20px;height:20px}
.card-white .web{bottom:26px;color:var(--ink)}

/* envelope */
.envelope{left:540px;top:360px;width:631px;height:353px}
.envelope .flap-brand{left:0;right:0;justify-content:center;top:20px;font-size:18px}
.envelope .flap-brand .mark{width:16px;height:16px}
.envelope .body-brand{left:24px;top:112px;font-size:28px}
.envelope .body-brand .mark{width:26px;height:26px}
.envelope .contact{left:24px;top:214px}
.envelope .faint-mark{left:470px;top:150px;width:80px;height:80px}
.envelope .web{bottom:14px;color:#fff}
</style>
</head>
<body>

<section class="piece letterhead">
  <svg class="shape" width="552" height="763" viewBox="0 0 552 763" aria-hidden="true">
    <path d="M0 718 Q276 690 552 700 V763 H0 Z" fill="var(--light-grey)"/>
    <path d="M0 730 Q276 708 552 716 V763 H0 Z" fill="var(--red)"/>
  </svg>
  <div class="brand brand-dark"><span class="mark"></span>Cordavera Ruvek</div>
  <address class="contact">
    2671 Bramble Rd, Lindenport, MI 48215<br>
    <b>Phone</b> : 555 014 2290<br>
    <b>Cell</b> : 555 014 2291<br>
    <b>Email</b> : info@cordaverix.example
  </address>
  <div class="faint-mark"></div>
  <div class="web">www.cordaverix.example</div>
</section>

<section class="piece card card-red">
  <div class="brand brand-white"><span class="mark"></span>Cordavera Ruvek</div>
  <div class="web">www.cordaverix.example</div>
</section>

<section class="piece card card-front">
  <svg class="shape" width="348" height="206" viewBox="0 0 348 206" aria-hidden="true">
    <path d="M132 0 C116 70 200 140 348 150 V160 C196 152 110 84 124 0 Z" fill="var(--grey)"/>
    <path d="M0 0 H120 C108 84 196 154 348 162 V206 H0 Z" fill="var(--red)"/>
  </svg>
  <div class="owner">
    <h1>Cordavera Ruvek</h1>
    <p>Disciplined Strength</p>
  </div>
  <div class="brand brand-dark"><span class="mark"></span>Cordavera Ruvek</div>
  <address class="contact">
    2671 Bramble Rd<br>
    Lindenport, MI 48215<br>
    <b>Phone</b> : 555 014 2290<br>
    <b>Cell</b> : 555 014 2291<br>
    <b>Email</b> : info@cordaverix.example
  </address>
</section>

<section class="piece card card-white">
  <div class="brand brand-dark"><span class="mark"></span>Cordavera Ruvek</div>
  <div class="web">www.cordaverix.example</div>
</section>

<section class="piece envelope">
  <svg class="shape" width="631" height="353" viewBox="0 0 631 353" aria-hidden="true">
    <path d="M0 0 H631 V62 Q315 84 0 62 Z" fill="var(--red)"/>
    <path d="M0 300 Q315 280 631 290 V353 H0 Z" fill="var(--light-grey)"/>
    <path d="M0 312 Q315 294 631 304 V353 H0 Z" fill="var(--red)"/>
  </svg>
  <div class="brand brand-white flap-brand"><span class="mark"></span>Cordavera Ruvek</div>
  <div class="brand brand-dark body-brand"><span class="mark"></span>Cordavera Ruvek</div>
  <address class="contact">
    2671 Bramble Rd<br>
    Lindenport, MI 48215<br>
    <b>Phone</b> : 555 014 2290<br>
    <b>Cell</b> : 555 014 2291<br>
    <b>Email</b> : info@cordaverix.example
  </address>
  <div class="faint-mark"></div>
  <div class="web">www.cordaverix.example</div>
</section>

</body>
</html>
```